Letterhead Design Project

We have recently updated our corporate logo and are seeking a new letterhead template.

Attached is the new logo and the old letterhead.

PLEASE DO NOT USE OUR EXISTING WEB SITE FOR INSPIRATION as we are redesigning it.

Target Market(s)

Executives, search professionals, technical and scientific professionals

Industry/Entity Type

Seeking

```html
<!DOCTYPE html>
<html lang="en">
<head>
<meta charset="utf-8">
<title>HelixSeek Letterhead</title>
<link rel="stylesheet" href="https://fonts.googleapis.com/css2?family=Source+Sans+3:wght@400;600&display=swap">
<style>
  :root {
    --brand-blue: #1a93cc;
    --brand-slate: #646970;
    --paper: #ffffff;
    --footer-text: #ffffff;
  }
  html, body {
    margin: 0;
    padding: 0;
    overflow: hidden;
    background: var(--paper);
  }
  .letterhead {
    position: relative;
    width: 927px;
    height: 1200px;
    overflow: hidden;
    background: var(--paper);
    font-family: "Source Sans 3", sans-serif;
  }
  .brand {
    position: absolute;
    left: 26px;
    top: 30px;
    display: flex;
    align-items: center;
    gap: 10px;
  }
  .brand-dot {
    width: 56px;
    height: 56px;
    border-radius: 50%;
    background: var(--brand-blue);
  }
  .brand-name {
    font-size: 46px;
    font-weight: 600;
    color: var(--brand-blue);
    letter-spacing: -0.5px;
    line-height: 1;
  }
  .web-address {
    position: absolute;
    right: 43px;
    top: 59px;
    font-size: 16.5px;
    color: var(--brand-blue);
  }
  .footer-band {
    position: absolute;
    left: 0;
    top: 0;
    width: 927px;
    height: 1200px;
  }
  .footer-mark {
    position: absolute;
    left: 36px;
    top: 1060px;
    width: 112px;
    height: 112px;
    border-radius: 50%;
    background: var(--paper);
  }
  .footer-contact {
    position: absolute;
    left: 0;
    width: 927px;
    top: 1142px;
    text-align: center;
    color: var(--footer-text);
    font-size: 14.5px;
    line-height: 19px;
  }
  .footer-contact .sep { padding: 0 4px; }
</style>
</head>
<body>
<div class="letterhead">
  <header>
    <div class="brand">
      <span class="brand-dot"></span>
      <span class="brand-name">HelixSeek</span>
    </div>
    <div class="web-address">www.helixseek.com</div>
  </header>

  <svg class="footer-band" viewBox="0 0 927 1200" aria-hidden="true">
    <defs>
      <linearGradient id="footerFade" x1="0" y1="0" x2="1" y2="0">
        <stop offset="0" stop-color="var(--brand-blue)" style="stop-color:#1593cd"/>
        <stop offset="1" stop-color="var(--brand-slate)" style="stop-color:#646970"/>
      </linearGradient>
    </defs>
    <path d="M0 985 Q470 1200 927 1083 L927 1200 L0 1200 Z" fill="url(#footerFade)"/>
  </svg>

  <footer>
    <div class="footer-mark"></div>
    <div class="footer-contact">
      <div>2400 Lakeview Parkway, Suite 310<span class="sep">•</span>Northfield, MA 01360</div>
      <div>Phone 508.555.0142 <span class="sep">•</span>Fax 508.555.0143</div>
    </div>
  </footer>
</div>
</body>
</html>
```